Business Card

I need a business card that really pops for a potential customer or person who refers a personal injury lead. I want to highlight our office locations, but only address that needs to be on the card is my office's main address. I want a sleek, modern and minimalist design.

```html
<!DOCTYPE html>
<html lang="en">
<head>
<meta charset="utf-8">
<title>Lantern Injury Lawyers — Business Card</title>
<link rel="stylesheet" href="https://fonts.googleapis.com/css2?family=Jost:wght@400;500&display=swap">
<style>
  :root {
    --page-bg: #e6e7e9;
    --charcoal: #3a3a3a;
    --silver: #ececec;
    --paper: #ffffff;
    --ink: #3a3a3a;
  }
  * { margin: 0; padding: 0; box-sizing: border-box; }
  html, body {
    width: 1200px;
    height: 1200px;
    overflow: hidden;
    background: var(--page-bg);
    font-family: "Jost", "Futura", sans-serif;
  }
  .canvas {
    position: relative;
    width: 1200px;
    height: 1200px;
  }
  .card {
    position: absolute;
    left: 265px;
    width: 692px;
    height: 405px;
  }
  .card-front {
    top: 130px;
    background: var(--charcoal);
  }
  .card-back {
    top: 650px;
    background: var(--paper);
  }

  /* Firm name, front */
  .front-name {
    position: absolute;
    left: 40px;
    right: 40px;
    top: 0;
    height: 335px;
    display: flex;
    align-items: center;
    justify-content: center;
    text-align: center;
    color: var(--silver);
    font-size: 54px;
    font-weight: 400;
    line-height: 1.1;
  }

  /* Firm name, back */
  .back-name {
    position: absolute;
    left: 40px;
    width: 308px;
    top: 130px;
    height: 110px;
    display: flex;
    align-items: center;
    justify-content: center;
    text-align: center;
    color: var(--ink);
    font-size: 34px;
    font-weight: 400;
    line-height: 1.15;
  }

  /* Contact block */
  .contact {
    position: absolute;
    left: 379px;
    top: 86px;
    color: var(--ink);
  }
  .contact .person-name {
    font-size: 25px;
    font-weight: 500;
    line-height: 1;
  }
  .contact .person-title {
    margin-top: 7px;
    font-size: 19px;
    font-weight: 400;
    line-height: 1;
  }
  .contact-list {
    list-style: none;
    margin-top: 27px;
  }
  .contact-item {
    display: flex;
    align-items: center;
    height: 20px;
    margin-bottom: 19px;
    font-size: 17px;
    letter-spacing: 0.01em;
  }
  .contact-item svg {
    width: 16px;
    height: 18px;
    margin-right: 9px;
    flex: none;
  }

  /* Address band */
  .address-band {
    position: absolute;
    left: 0;
    right: 0;
    top: 347px;
    height: 31px;
    background: var(--charcoal);
    color: var(--paper);
    font-size: 16px;
    letter-spacing: 0.02em;
    display: flex;
    align-items: center;
    justify-content: center;
  }
</style>
</head>
<body>
<main class="canvas">
  <section class="card card-front">
    <p class="front-name">Lantern Injury Lawyers</p>
  </section>

  <section class="card card-back">
    <p class="back-name">Lantern<br>Injury Lawyers</p>

    <div class="contact">
      <p class="person-name">YOUR NAME</p>
      <p class="person-title">Title</p>
      <ul class="contact-list">
        <li class="contact-item">
          <svg viewBox="0 0 16 18" aria-hidden="true">
            <rect x="3.5" y="0.8" width="9" height="16.4" rx="1.6" fill="none" stroke="#3a3a3a" stroke-width="1.4"/>
            <line x1="3.5" y1="13.6" x2="12.5" y2="13.6" stroke="#3a3a3a" stroke-width="1.2"/>
            <circle cx="8" cy="15.4" r="0.8" fill="#3a3a3a"/>
          </svg>
          <span>0123456789</span>
        </li>
        <li class="contact-item">
          <svg viewBox="0 0 16 18" aria-hidden="true">
            <rect x="0.5" y="4" width="15" height="10.5" fill="#3a3a3a"/>
            <polyline points="0.8,4.4 8,10 15.2,4.4" fill="none" stroke="#ffffff" stroke-width="1.2"/>
            <line x1="0.8" y1="14.2" x2="6" y2="9" stroke="#ffffff" stroke-width="1"/>
            <line x1="15.2" y1="14.2" x2="10" y2="9" stroke="#ffffff" stroke-width="1"/>
          </svg>
          <span>youremailaddress@lanternlaw.com</span>
        </li>
        <li class="contact-item">
          <svg viewBox="0 0 16 18" aria-hidden="true">
            <g fill="none" stroke="#3a3a3a" stroke-width="1.2">
              <circle cx="8" cy="9" r="7"/>
              <ellipse cx="8" cy="9" rx="3" ry="7"/>
              <line x1="1" y1="9" x2="15" y2="9"/>
              <line x1="2" y1="5.5" x2="14" y2="5.5"/>
              <line x1="2" y1="12.5" x2="14" y2="12.5"/>
              <line x1="8" y1="2" x2="8" y2="16"/>
            </g>
          </svg>
          <span>www.lanternlaw.com</span>
        </li>
      </ul>
    </div>

    <div class="address-band">Your Company Address Will Be Given Here</div>
  </section>
</main>
</body>
</html>
```